KTR Associates Business Card

I would like to have a business card designed that uses my current logo and colors. I am not looking for anything to "out there" but can have a little fun so that it stands out.

I have a boutique consulting firm that specializes in strategic planning, change management, leadership development and innovation.

Industry/Entity Type

Leadership

Contact Information for Business Card

Marta Holloway
President
marta@ktr-associates-mail.com
919-555-0143

```html
<!DOCTYPE html>
<html lang="en">
<head>
<meta charset="utf-8">
<title>KTR Associates Business Card</title>
<link rel="stylesheet" href="https://fonts.googleapis.com/css2?family=Jost:wght@400;500;600&display=swap">
<style>
  :root {
    --page: #e6e5e2;
    --ink: #111111;
    --paper: #ffffff;
    --black-card: #0d0d0d;
    --logo-light: #e9e9e6;
    --green: #2e9a5a;
    --green-deep: #1f6e3c;
    --green-light: #a9cf55;
    --text-soft: #2a2a2a;
  }
  * { margin: 0; padding: 0; box-sizing: border-box; }
  html, body { width: 1200px; height: 871px; overflow: hidden; }
  body {
    background: var(--page);
    font-family: "Jost", Arial, sans-serif;
    position: relative;
  }
  .card { position: absolute; box-shadow: 0 6px 18px rgba(0,0,0,0.18); }

  /* Front */
  .card-front {
    left: 70px; top: 285px;
    width: 525px; height: 300px;
    background: var(--black-card);
    display: flex; align-items: center; justify-content: center;
  }
  .logo { font-weight: 400; text-align: center; line-height: 1; }
  .card-front .logo { color: var(--logo-light); }
  .logo-name { display: block; font-size: 74px; letter-spacing: 2px; }
  .logo-sub { display: block; font-size: 13px; letter-spacing: 9px; margin-top: 12px; padding-left: 9px; }

  /* Back */
  .card-back {
    left: 700px; top: 173px;
    width: 300px; height: 525px;
    background: var(--paper);
    overflow: hidden;
  }
  .card-back .logo {
    position: absolute; left: 36px; top: 46px;
    color: var(--ink); text-align: left;
  }
  .card-back .logo-name { font-size: 66px; }
  .card-back .logo-sub { font-size: 11px; letter-spacing: 7px; padding-left: 2px; margin-top: 10px; }

  .person { position: absolute; left: 36px; top: 250px; }
  .person-name { font-size: 15px; font-weight: 600; letter-spacing: 2.5px; color: var(--ink); }
  .person-title { font-size: 9px; font-weight: 600; letter-spacing: 1.5px; color: var(--green); margin-top: 4px; text-transform: uppercase; }

  .contact-list { position: absolute; left: 36px; top: 312px; list-style: none; }
  .contact-item {
    display: flex; align-items: center; gap: 9px;
    font-size: 10.5px; letter-spacing: 1.5px; color: var(--text-soft);
    margin-bottom: 8px; text-transform: uppercase; white-space: nowrap;
  }
  .contact-icon { width: 12px; height: 12px; flex: none; }

  .brush-band {
    position: absolute; left: 0; right: 0; bottom: 44px; height: 34px;
    background: linear-gradient(90deg, var(--green-light), var(--green) 55%, var(--green-deep));
  }
  .footer-band {
    position: absolute; left: 0; right: 0; bottom: 0; height: 44px;
    background: var(--black-card);
    display: flex; align-items: center; justify-content: center;
  }
  .footer-web { color: var(--paper); font-size: 10px; letter-spacing: 2.5px; text-transform: uppercase; }
</style>
</head>
<body>
  <section class="card card-front">
    <div class="logo">
      <span class="logo-name">KTR</span>
      <span class="logo-sub">ASSOCIATES</span>
    </div>
  </section>

  <section class="card card-back">
    <div class="logo">
      <span class="logo-name">KTR</span>
      <span class="logo-sub">ASSOCIATES</span>
    </div>

    <div class="person">
      <p class="person-name">MARTA HOLLOWAY</p>
      <p class="person-title">President</p>
    </div>

    <ul class="contact-list">
      <li class="contact-item">
        <svg class="contact-icon" viewBox="0 0 12 12"><circle cx="6" cy="6" r="6" fill="#2e9a5a"/><path d="M4 3.2 L5 3 L5.6 4.6 L4.9 5.1 Q5.5 6.6 6.9 7.1 L7.4 6.4 L9 7 L8.8 8 Q6.8 8.6 5 7 Q3.4 5.3 4 3.2Z" fill="#fff"/></svg>
        919-555-0143
      </li>
      <li class="contact-item">
        <svg class="contact-icon" viewBox="0 0 12 12"><circle cx="6" cy="6" r="6" fill="#2e9a5a"/><rect x="3" y="4" width="6" height="4.2" fill="none" stroke="#fff" stroke-width="0.8"/><path d="M3 4 L6 6.4 L9 4" fill="none" stroke="#fff" stroke-width="0.8"/></svg>
        marta@ktr-associates-mail.com
      </li>
      <li class="contact-item">
        <svg class="contact-icon" viewBox="0 0 12 12"><circle cx="6" cy="6" r="6" fill="#2e9a5a"/><circle cx="6" cy="6" r="3.2" fill="none" stroke="#fff" stroke-width="0.7"/><ellipse cx="6" cy="6" rx="1.4" ry="3.2" fill="none" stroke="#fff" stroke-width="0.7"/><path d="M2.8 6 H9.2" stroke="#fff" stroke-width="0.7"/></svg>
        www.ktrassociates-mail.com
      </li>
    </ul>

    <div class="brush-band" role="img" aria-label="Green brush-stroke texture band"></div>
    <div class="footer-band">
      <p class="footer-web">www.ktrassociates-mail.com</p>
    </div>
  </section>
</body>
</html>
```